Develop a Corporate Identity for Marlowquest

Looking for a
1. Powerpoint Template
2. Stationery / Letterhead
3. Presentation Folder
4. Business Card

Learn more about the company here at [url removed, login to view] The focus of the brand needs to be on the wheel (or a circle in general) regarding both attached logos as we intend to show that we are a complete training solution. The items must also work with BOTH attached logos.

```html
<!DOCTYPE html>
<html lang="en">
<head>
<meta charset="utf-8">
<title>Marlowquest Presentation Folder</title>
<link rel="stylesheet" href="https://fonts.googleapis.com/css2?family=Questrial&family=Roboto+Condensed:wght@400&display=swap">
<style>
  :root {
    --charcoal: #4d4d4c;
    --orange: #f7941d;
    --paper: #ffffff;
    --backdrop: #f1f1f1;
    --fold: #9a9a9a;
    --ink-light: #ffffff;
  }
  html, body {
    margin: 0;
    padding: 0;
    width: 1200px;
    height: 872px;
    overflow: hidden;
    background: var(--backdrop);
  }
  .folder-spread {
    display: block;
    width: 1200px;
    height: 872px;
  }
  .page { fill: var(--paper); }
  .panel-dark { fill: var(--charcoal); }
  .ring-orange { fill: var(--orange); }
  .ring-inner { fill: var(--paper); }
  .fold-line { stroke: var(--fold); stroke-width: 0.6; }
  .brand-dot { fill: var(--orange); }
  .brand-name {
    font-family: "Questrial", sans-serif;
    font-size: 23px;
    fill: var(--charcoal);
    letter-spacing: -0.3px;
  }
  .contact-details {
    font-family: "Roboto Condensed", sans-serif;
    font-size: 5.4px;
    fill: var(--ink-light);
  }
  .web-address {
    font-family: "Roboto Condensed", sans-serif;
    font-size: 5.4px;
    fill: var(--charcoal);
  }
</style>
</head>
<body>
<svg class="folder-spread" viewBox="0 0 800 581.33" xmlns="http://www.w3.org/2000/svg">
  <!-- pages -->
  <rect class="page back-cover" x="27" y="33" width="365" height="508"/>
  <rect class="page front-cover" x="392" y="33" width="363" height="508"/>

  <!-- back cover dark panel, running over the fold at the top -->
  <rect class="panel-dark" x="27" y="33" width="365" height="508"/>
  <rect class="panel-dark" x="391" y="33" width="22" height="200"/>

  <!-- wheel on the front cover -->
  <clipPath id="front-clip">
    <rect x="380" y="33" width="375" height="508"/>
  </clipPath>
  <g class="wheel" clip-path="url(#front-clip)">
    <circle class="panel-dark" cx="572" cy="298" r="181"/>
    <rect class="panel-dark" x="560" y="455" width="195" height="24"/>
    <circle class="ring-orange" cx="573" cy="302" r="160"/>
    <circle class="ring-inner" cx="573" cy="302" r="133"/>
  </g>

  <line class="fold-line" x1="392" y1="10" x2="392" y2="560"/>

  <!-- brand -->
  <circle class="brand-dot" cx="566" cy="274" r="16"/>
  <text class="brand-name" x="574" y="321" text-anchor="middle">Marlowquest</text>

  <!-- back cover contact block -->
  <text class="contact-details" text-anchor="middle">
    <tspan x="210" y="491">Floor/Plot #, Street Name, Town Name, State Name,</tspan>
    <tspan x="210" y="498">Country Name, Office Tel no, Fax, Email Web address</tspan>
    <tspan x="210" y="505">(we can use icons for  email, fax, web)</tspan>
  </text>

  <!-- front cover web address -->
  <text class="web-address" x="568" y="509" text-anchor="middle">www.marlowquest.com</text>
</svg>
</body>
</html>
```